BrightNomadRx.com Blog Design (Travel, Lifestyle, and Life Hacking blog)

I am launching a lifestyle blog about my life. I'm a doctor who travels the world trying the best restaurants, airlines and trying to have as much fun as possible. I also invest in startups, and am always trying new tricks to make life better. I also plan to write about various other topics, but essentially it is about travel, lifestyle and medicine. I need a creative and really awesome looking design for a new wordpress blog called BrightNomadRx

Target Market(s)

Physicians, Entrepreneurs, Travellers

Industry/Entity Type

Airlines

Number of Pages Required

1 page

Font styles to use
Serif

Requirements
Must have
• Slick looking graphics with a highly professional modern feel

```html
<!DOCTYPE html>
<html lang="en">
<head>
<meta charset="utf-8">
<title>BrightNomadRx</title>
<link href="https://fonts.googleapis.com/css2?family=Lato:wght@400;700;900&display=swap" rel="stylesheet">
<style>
:root{
  --accent:#9a7b4f;
  --ink:#2f2f2f;
  --text:#555;
  --muted:#777;
  --rule:#d9d9d9;
  --topbar:#f0f0f0;
  --footer:#333;
  --white:#fff;
}
*{margin:0;padding:0;box-sizing:border-box}
html,body{width:678px;height:1200px;overflow:hidden;background:var(--white)}
body{position:relative;font-family:'Lato',sans-serif;color:var(--ink)}
.abs{position:absolute}
.topbar{left:0;top:0;width:678px;height:18px;background:var(--topbar)}
.search-hint{left:105px;top:5px;font-size:6px;color:var(--muted)}
.topbar-divider{left:520px;top:0;width:1px;height:18px;background:var(--rule)}
.topbar-divider.r{left:567px}
.social{display:flex;gap:5px}
.social i{display:block;width:6px;height:6px;border-radius:50%;background:var(--muted)}
.social.brown i{background:var(--accent)}
.social.dark i{background:var(--ink)}
.social.light i{background:#ddd}
.brand{left:0;top:26px;width:678px;text-align:center;font-size:25px;font-weight:900;color:var(--accent);letter-spacing:.5px}
.hero{left:0;top:62px;width:678px;height:252px;background:linear-gradient(180deg,#9fb8c4 0%,#7fb0bd 28%,#c9c2b4 55%,#d8cfc0 100%)}
.hero-panel{left:162px;top:131px;width:355px;height:127px;background:rgba(45,45,45,.72);text-align:center;color:var(--white)}
.hero-title{margin-top:26px;font-size:15px;font-weight:400;letter-spacing:.3px}
.hero-rule{width:175px;height:1px;background:rgba(255,255,255,.6);margin:7px auto 10px}
.hero-text{font-size:8px;line-height:13px;padding:0 10px}
.tile{top:338px;width:148px;height:100px;display:flex;align-items:center;justify-content:center;color:var(--white);font-size:12px;font-weight:700}
.tile span{position:relative}
.tile.lifestyle{left:91px;background:linear-gradient(180deg,#6f9db8,#a9c1c9 60%,#d9cbb2)}
.tile.travel{left:265px;background:linear-gradient(180deg,#7fa6b8,#b9ad95 55%,#d7c7a8)}
.tile.medicine{left:438px;background:linear-gradient(135deg,#3d6273,#86a4b1 60%,#b9c9cf)}
.photo{display:block}
.meta{font-size:6.5px;color:var(--ink)}
.cal{display:inline-block;width:7px;height:6px;border:1px solid var(--accent);vertical-align:-1px;margin-right:6px}
.cmt{display:inline-block;width:8px;height:6px;border:1px solid var(--muted);border-radius:4px;vertical-align:-1px;margin-right:3px}
.feat-title{left:91px;top:649px;width:322px;text-align:center;font-size:10px;font-weight:700}
.feat-text{left:95px;top:667px;width:314px;text-align:center;font-size:6.3px;line-height:11.5px;color:var(--text)}
.btn{background:var(--accent);color:var(--white);font-size:7px;display:flex;align-items:center;justify-content:center}
.post-title{font-size:9px;font-weight:700}
.post-text{font-size:6.3px;line-height:10.5px;color:var(--text);width:175px}
.sep{height:1px;background:var(--rule)}
.side-h{left:438px;font-size:7.5px;font-weight:700}
.side-text{left:438px;top:482px;width:150px;font-size:6.3px;line-height:11.5px;color:var(--text);letter-spacing:.3px}
.latest{left:438px;width:150px;display:flex;gap:6px}
.latest .thumb{width:37px;height:35px;flex:none}
.latest p{font-size:5.8px;line-height:9px;font-weight:700}
.latest small{display:block;font-weight:400;font-size:5.5px}
.list{left:438px;font-size:5.8px;font-weight:700;line-height:14.5px;list-style:none}
.list li::before{content:"";display:inline-block;width:8px;height:1px;background:var(--muted);vertical-align:2px;margin-right:3px}
.list.arch{line-height:17.6px}
.input{left:438px;top:785px;width:148px;height:18px;border:1px solid #bbb;background:#f2f2f2}
.pager{font-size:6.5px;color:var(--muted)}
.footer{left:0;top:1174px;width:678px;height:26px;background:var(--footer)}
.copyright{left:92px;top:10px;font-size:6.5px;color:#ddd}
</style>
</head>
<body>

<header>
  <div class="abs topbar">
    <svg class="abs" style="left:92px;top:4px" width="9" height="9" viewBox="0 0 9 9"><circle cx="3.6" cy="3.6" r="2.7" fill="none" stroke="#333" stroke-width="1.3"/><line x1="5.6" y1="5.6" x2="8.3" y2="8.3" stroke="#333" stroke-width="1.4"/></svg>
    <span class="abs search-hint">Type to search...</span>
    <div class="abs topbar-divider"></div>
    <div class="abs social brown" style="left:528px;top:6px"><i></i><i></i><i></i></div>
    <div class="abs topbar-divider r"></div>
    <svg class="abs" style="left:575px;top:5px" width="12" height="8" viewBox="0 0 12 8"><g fill="#9a7b4f"><rect x="0" y="0" width="2" height="1.5"/><rect x="3" y="0" width="9" height="1.5"/><rect x="0" y="3.2" width="2" height="1.5"/><rect x="3" y="3.2" width="9" height="1.5"/><rect x="0" y="6.4" width="2" height="1.5"/><rect x="3" y="6.4" width="9" height="1.5"/></g></svg>
  </div>
  <div class="abs brand">BrightNomadRx</div>
</header>

<section class="abs hero" role="img" aria-label="Couple relaxing on beach loungers by the sea with overwater bungalows">
</section>
<div class="abs hero-panel">
  <h1 class="hero-title">NEW TRICKS TO MAKE LIFE BETTER</h1>
  <div class="hero-rule"></div>
  <p class="hero-text">Lorem ipsum dolor sit amet, consectetuer adipiscing elit, sed diam nonummy nibh euismod tincidunt ut laoreet dolore magna aliquam erat volutpat. Ut wisi enim ad minim veniam, quis nostrud exerci tation ullamcorper suscipit lobortis nisl ut aliquip</p>
</div>

<nav>
  <div class="abs tile lifestyle" role="img" aria-label="Family walking on a beach"><span>LIFESTYLE</span></div>
  <div class="abs tile travel" role="img" aria-label="Sun hat and beach bag on the sand"><span>TRAVEL</span></div>
  <div class="abs tile medicine" role="img" aria-label="Glass globe with a stethoscope"><span>MEDICINE</span></div>
</nav>

<main>
  <div class="abs photo" style="left:91px;top:464px;width:322px;height:157px;background:linear-gradient(180deg,#5d7a4a,#8ea77a 45%,#6d7a5a 75%,#8d9a80)" role="img" aria-label="Traveller with backpack and straw hat walking through a jungle"></div>
  <div class="abs meta" style="left:92px;top:628px"><span class="cal"></span>December 25, 2016</div>
  <div class="abs meta" style="left:397px;top:627px"><span class="cmt"></span>1</div>
  <h2 class="abs feat-title">Lorem Ipsum Dolor Sit Amet, Consectetuer Adipiscing Elit</h2>
  <p class="abs feat-text">Lorem ipsum dolor sit amet, consectetuer adipiscing elit, sed diam nonummy nibh euismod tincidunt ut laoreet dolore magna aliquam erat volutpat. Ut wisi enim ad minim veniam, quis nostrud exerci tation ullamcorper suscipit lobortis nisl ut aliquip</p>
  <div class="abs btn" style="left:183px;top:710px;width:60px;height:19px">Read More</div>
  <div class="abs social dark" style="left:261px;top:717px;gap:10px"><i></i><i></i><i></i><i></i></div>

  <article>
    <div class="abs photo" style="left:91px;top:772px;width:141px;height:80px;background:linear-gradient(180deg,#9fb0c0,#b79a7c 45%,#b0704a)" role="img" aria-label="Hiker with orange backpack reading a tablet on a canyon edge"></div>
    <h3 class="abs post-title" style="left:240px;top:772px">Lorem Ipsum Dolor Sit Amet</h3>
    <div class="abs social dark" style="left:241px;top:788px;gap:4px"><i></i><i></i><i></i><i></i></div>
    <p class="abs post-text" style="left:240px;top:802px">Lorem ipsum dolor sit amet, consectetuer adipiscing elit, sed diam nonummy nibh euismod tincidunt ut laoreet dolore magna aliquam erat volutpat.</p>
    <div class="abs btn" style="left:239px;top:843px;width:60px;height:17px">Read More</div>
    <div class="abs meta" style="left:92px;top:857px"><span class="cal"></span>December 25, 2016</div>
    <div class="abs meta" style="left:217px;top:857px"><span class="cmt"></span>1</div>
    <div class="abs sep" style="left:91px;top:879px;width:322px"></div>
  </article>

  <article>
    <div class="abs photo" style="left:91px;top:895px;width:141px;height:80px;background:linear-gradient(90deg,#c8cfd6,#e9e6df 50%,#a7b0ba)" role="img" aria-label="Traveller with suitcase on an airport walkway"></div>
    <h3 class="abs post-title" style="left:240px;top:895px">Lorem Ipsum Dolor Sit Amet</h3>
    <div class="abs social dark" style="left:241px;top:911px;gap:4px"><i></i><i></i><i></i><i></i></div>
    <p class="abs post-text" style="left:240px;top:925px">Lorem ipsum dolor sit amet, consectetuer adipiscing elit, sed diam nonummy nibh euismod tincidunt ut laoreet dolore magna aliquam erat volutpat.</p>
    <div class="abs btn" style="left:239px;top:966px;width:60px;height:17px">Read More</div>
    <div class="abs meta" style="left:92px;top:980px"><span class="cal"></span>December 25, 2016</div>
    <div class="abs meta" style="left:217px;top:980px"><span class="cmt"></span>1</div>
    <div class="abs sep" style="left:91px;top:1002px;width:322px"></div>
  </article>

  <article>
    <div class="abs photo" style="left:91px;top:1018px;width:141px;height:80px;background:linear-gradient(180deg,#4f8fc6,#5fb4c8 45%,#e4d6b8)" role="img" aria-label="Resort beach with loungers and parasols"></div>
    <h3 class="abs post-title" style="left:240px;top:1018px">Lorem Ipsum Dolor Sit Amet</h3>
    <div class="abs social dark" style="left:241px;top:1034px;gap:4px"><i></i><i></i><i></i><i></i></div>
    <p class="abs post-text" style="left:240px;top:1048px">Lorem ipsum dolor sit amet, consectetuer adipiscing elit, sed diam nonummy nibh euismod tincidunt ut laoreet dolore magna aliquam erat volutpat.</p>
    <div class="abs btn" style="left:239px;top:1089px;width:60px;height:17px">Read More</div>
    <div class="abs meta" style="left:92px;top:1103px"><span class="cal"></span>December 25, 2016</div>
    <div class="abs meta" style="left:217px;top:1103px"><span class="cmt"></span>1</div>
  </article>

  <div class="abs sep" style="left:91px;top:1138px;width:322px"></div>
  <div class="abs pager" style="left:91px;top:1142px"><span style="color:var(--accent)">&#8592;</span> Older Posts</div>
  <div class="abs pager" style="left:358px;top:1142px">Newer Posts <span style="color:var(--accent)">&#8594;</span></div>
</main>

<aside>
  <h4 class="abs side-h" style="top:465px">About Me</h4>
  <p class="abs side-text">Lorem ipsum dolor sit amet, consectetuer adipiscing elit, sed diam nonummy nibh euismod tincidunt ut laoreet dolore magna aliquam erat volutpat. Ut wisi enim ad minim veniam.</p>
  <div class="abs btn" style="left:438px;top:537px;width:60px;height:16px">Read More</div>
  <div class="abs social dark" style="left:438px;top:566px;gap:8px"><i></i><i></i><i></i><i></i></div>
  <div class="abs sep" style="left:438px;top:585px;width:148px"></div>

  <h4 class="abs side-h" style="top:598px">Latest Posts</h4>
  <div class="abs latest" style="top:620px"><div class="thumb" style="background:linear-gradient(180deg,#6d8a5a,#a08a66)" role="img" aria-label="Backpacker in jungle"></div><p>Lorem Ipsum is simply du of sed diam nonummy the printing.<small>September 9, 2016</small></p></div>
  <div class="abs latest" style="top:668px"><div class="thumb" style="background:linear-gradient(180deg,#9fb0c0,#b0704a)" role="img" aria-label="Hiker on canyon edge"></div><p>Lorem Ipsum is simply du of sed diam nonummy the printing.<small>September 9, 2016</small></p></div>
  <div class="abs latest" style="top:716px"><div class="thumb" style="background:linear-gradient(90deg,#c8cfd6,#a7b0ba)" role="img" aria-label="Traveller in airport"></div><p>Lorem Ipsum is simply du of sed diam nonummy the printing.<small>September 9, 2016</small></p></div>
  <div class="abs sep" style="left:438px;top:761px;width:135px;background:#eee"></div>

  <h4 class="abs side-h" style="top:772px">Search</h4>
  <div class="abs input"></div>
  <div class="abs btn" style="left:438px;top:810px;width:148px;height:15px">Search</div>
  <div class="abs sep" style="left:438px;top:839px;width:148px"></div>

  <h4 class="abs side-h" style="top:852px">Categories</h4>
  <ul class="abs list" style="top:864px">
    <li>Uncategorized</li>
    <li>It is a long established fact that a reader.</li>
    <li>Ducimus qui blanditiis.</li>
  </ul>
  <div class="abs sep" style="left:438px;top:918px;width:148px"></div>

  <h4 class="abs side-h" style="top:930px">Archives</h4>
  <ul class="abs list arch" style="top:943px">
    <li>December 2016</li><li>November 2016</li><li>October 2016</li><li>September 2016</li>
    <li>August 2016</li><li>July 2016</li><li>June 2016</li><li>May 2016</li>
    <li>April 2016</li><li>March 2016</li><li>February 2016</li><li>January 2016</li>
  </ul>
</aside>

<footer class="abs footer">
  <p class="abs copyright">Copyright © 2016 BrightNomadRx. All rights reserved.</p>
  <div class="abs social light" style="left:548px;top:10px"><i></i><i></i><i></i><i></i></div>
</footer>

</body>
</html>
```